Coloring book cover design: Shade It, Crease It coloring book, Christmas edition Volume 1

I need a cover design [front and back please]] (book trim size: 8.5 x 11 inches) for my first coloring book titled "Shade it, crease it: coloring book (Christmas Edition)". The designs should include Christmassy colors (for example: green, red, gold and/or other colors but not more than 5 in total). Covers need to be sufficiently generic to maintain a recognizable design theme for other non-Christmassy forthcoming books/editions (i.e. familiar design theme across all books so customers know they come from the same author).
Updates

I have increased the budget for the 1st prize and updated the brief. This is the first in a series of books and the designs need to create a theme that is then repeated across future editions and volumes. Added Friday, August 26, 2016

Target Market(s)

Mostly women (age: 25+).

Industry/Entity Type

Graphic Art

Font styles to use
Serif
Sans Serif
Decorative

Requirements
Must have
• The cover design must include designs provided in separate JPEG/PSD files (these are from the book itself) so customers can sense what to expect from the book’s content. The supplied PSD files include paths so please play around with supplied files and take some motives from the overall patterns.
Nice to have
• Some nice features that will make it stand out from the crowd of recent coloring book covers. I will let the designer choose the colors but as stated, they have to be Christmassy.
• Some good examples from Hattie Brennock and Susan Pelworthy:
• https://img-store.example-shopzone.com/pics/I/72qd5mKjcEM._SX258_BO1,204,203,200_.jpg
• http://quietbrushwork.net/wp-content/uploads/2015/03/Screenshot-2015-12-16-12.07.06.png
Should not have
• Imported images of people, animals, etc. This is a coloring book and the cover must reflect this.

```html
<!DOCTYPE html>
<html lang="en">
<head>
<meta charset="utf-8">
<title>Shade It, Crease It – Coloring Book Cover</title>
<link href="https://fonts.googleapis.com/css2?family=Delius&family=Cinzel:wght@400;700&family=Tinos&display=swap" rel="stylesheet">
<style>
  :root {
    --bg: #d9d9d9;
    --paper: #ffffff;
    --red: #b3171b;
    --red-text: #d0151c;
    --green: #1f7a34;
    --green-soft: #cfe3d0;
    --red-soft: #f3c9c6;
    --pink: #e89a90;
    --white: #ffffff;
  }
  * { box-sizing: border-box; margin: 0; padding: 0; }
  html, body { width: 1200px; height: 934px; overflow: hidden; background: var(--bg); }
  .wrap { position: relative; width: 1200px; height: 934px; }
  .book { position: absolute; left: 52px; top: 130px; display: flex; height: 673px;
          box-shadow: 0 10px 30px rgba(0,0,0,.18); }
  .cover { position: relative; width: 520px; height: 673px; background: var(--paper); overflow: hidden; }
  .spine { position: relative; width: 56px; height: 673px; background: var(--red); }

  /* back cover */
  .back-intro { position: absolute; top: 38px; left: 30px; right: 30px; text-align: center;
                font-family: "Delius", cursive; font-size: 21px; line-height: 1.25; color: var(--red-text); }
  .back-title { position: absolute; top: 152px; left: 0; right: 0; text-align: center;
                font-family: "Delius", cursive; font-size: 46px; line-height: 1.02; color: var(--red-text); }
  .art { position: absolute; }
  .art-house { left: 22px; top: 150px; width: 90px; height: 80px; }
  .art-bell { right: 24px; top: 150px; width: 95px; height: 95px; }
  .back-band { position: absolute; top: 282px; left: 0; right: 0; height: 130px; background: var(--red);
               padding: 14px 34px; font-family: "Delius", cursive; font-size: 14.5px; line-height: 1.3; color: var(--white); }
  .art-net { left: 160px; top: 455px; width: 200px; height: 200px; }

  /* spine */
  .spine-text { position: absolute; left: 50%; top: 130px; transform: translateX(-50%);
                writing-mode: vertical-rl; font-family: "Delius", cursive; color: var(--white);
                white-space: nowrap; display: flex; gap: 22px; align-items: baseline; }
  .spine-title { font-size: 27px; }
  .spine-author { font-size: 21px; }
  .spine-star { position: absolute; left: 10px; width: 36px; height: 36px; }
  .spine-star.top { top: 60px; }
  .spine-star.bottom { bottom: 60px; }

  /* front cover */
  .art-lace-tl { left: -10px; top: 0; width: 180px; height: 150px; }
  .art-lace-tr { right: 0; top: 0; width: 150px; height: 150px; }
  .art-lace-bl { left: 0; bottom: 0; width: 170px; height: 140px; }
  .art-lace-br { right: 0; bottom: 20px; width: 160px; height: 140px; }
  .edition { position: absolute; top: 40px; left: 150px; width: 200px; text-align: center;
             font-family: "Tinos", serif; color: var(--green); }
  .edition .stars { color: var(--pink); font-size: 22px; letter-spacing: 6px; line-height: 1; }
  .edition .line1 { font-size: 17px; margin-top: 4px; }
  .edition .line2 { font-size: 15px; margin: 4px 0 6px; }
  .art-mandala { left: 70px; top: 175px; width: 390px; height: 390px; }
  .front-band { position: absolute; top: 305px; left: 0; right: 0; height: 140px; background: var(--red);
                text-align: center; color: var(--white); padding-top: 18px; }
  .front-author { font-family: "Delius", cursive; font-size: 18px; }
  .front-title { font-family: "Delius", cursive; font-size: 44px; line-height: 1.1; }
  .front-sub { font-family: "Cinzel", serif; font-size: 22px; letter-spacing: 1px; }
</style>
</head>
<body>
<div class="wrap">
  <div class="book">
    <section class="cover cover-back">
      <p class="back-intro">Lorem ipsum dolor sit amet, consectetur adipisicing elit, sed do eiusmod tempor incididunt ut labore</p>
      <svg class="art art-house" role="img" aria-label="Small green line illustration of a snowy cottage" viewBox="0 0 90 80">
        <rect width="90" height="80" rx="6" fill="#d6e8d8"/>
      </svg>
      <h2 class="back-title">Shade It<br>Crease It</h2>
      <svg class="art art-bell" role="img" aria-label="Green Christmas bell with ribbon illustration" viewBox="0 0 95 95">
        <rect width="95" height="95" rx="8" fill="#d6e8d8"/>
      </svg>
      <div class="back-band">Lorem ipsum dolor sit amet, consectetur adipisicing elit, sed do eiusmod tempor incididunt ut labore et dolore magna aliqua. Ut enim ad minim veniam, quis nostrud exercitation ullamco laboris nisi ut aliquip ex ea commodo consequat. Duis aute irure dolor in reprehenderit in voluptate velit esse</div>
      <svg class="art art-net" role="img" aria-label="Pale green patterned foldable cube net" viewBox="0 0 200 200">
        <polygon points="65,0 135,0 135,55 200,55 200,120 135,120 135,200 65,200 65,120 0,120 0,55 65,55" fill="#e3eee3" stroke="#b9d2bb"/>
      </svg>
    </section>

    <aside class="spine">
      <svg class="spine-star top" role="img" aria-label="Small pink star ornament" viewBox="0 0 36 36"><circle cx="18" cy="18" r="14" fill="#d96b5f"/></svg>
      <div class="spine-text"><span class="spine-title">Shade It, Crease It</span><span class="spine-author">Clara Whitfield</span></div>
      <svg class="spine-star bottom" role="img" aria-label="Small pink star ornament" viewBox="0 0 36 36"><circle cx="18" cy="18" r="14" fill="#d96b5f"/></svg>
    </aside>

    <section class="cover cover-front">
      <svg class="art art-lace-tl" role="img" aria-label="Green lace mandala circles" viewBox="0 0 180 150"><rect width="180" height="150" fill="#e2efe3"/></svg>
      <svg class="art art-lace-tr" role="img" aria-label="Red lace mandala circles" viewBox="0 0 150 150"><rect width="150" height="150" fill="#f8e1df"/></svg>
      <div class="edition">
        <div class="stars">✳✳✳</div>
        <div class="line1">Christmas Edition</div>
        <div class="line2">Volume 1</div>
        <div class="stars">✳✳✳</div>
      </div>
      <svg class="art art-mandala" role="img" aria-label="Large round mandala, left half green and right half red, ringed with red berries" viewBox="0 0 390 390">
        <defs>
          <linearGradient id="mandalaTone" x1="0" x2="1" y1="0" y2="0">
            <stop offset="0.5" stop-color="#4f9a5e"/>
            <stop offset="0.5" stop-color="#d9574f"/>
          </linearGradient>
        </defs>
        <circle cx="195" cy="195" r="190" fill="url(#mandalaTone)"/>
      </svg>
      <div class="front-band">
        <div class="front-author">Clara Whitfield</div>
        <h1 class="front-title">Shade It, Crease It</h1>
        <div class="front-sub">Coloring Book</div>
      </div>
      <svg class="art art-lace-bl" role="img" aria-label="Red lace mandala circles" viewBox="0 0 170 140"><rect width="170" height="140" fill="#f8e1df"/></svg>
      <svg class="art art-lace-br" role="img" aria-label="Green lace mandala circles" viewBox="0 0 160 140"><rect width="160" height="140" fill="#e2efe3"/></svg>
    </section>
  </div>
</div>
</body>
</html>
```